Local fast-growing company in the service sector

We are looking for a modern business card design, which should also appear on our letterheads

Target Market(s)

Private and industrial sectors

Contact Information for Business Card

Vorname Name
Lindkofer Str. 18
71468 Lindenbach
Tel.: 07163-418259-0
Name@kovaltec-pbz.de

Colors
9d9d9d
919191
aaaaaa

Requirements
Must have
• The logo (file) in silver

```html
<!DOCTYPE html>
<html lang="de">
<head>
<meta charset="utf-8">
<title>Kovaltec – Visitenkarte</title>
<link href="https://fonts.googleapis.com/css2?family=Lato:wght@400;700&display=swap" rel="stylesheet">
<style>
  :root {
    --page-bg: #e4e4e4;
    --card-bg: #ffffff;
    --silver: #9d9d9d;
    --silver-dark: #919191;
    --silver-light: #aaaaaa;
    --ink: #4a4a4a;
    --rule: #d2d2d2;
  }
  html, body {
    margin: 0;
    width: 1200px;
    height: 900px;
    overflow: hidden;
    background: var(--page-bg);
    font-family: "Lato", sans-serif;
  }
  .stage {
    width: 1200px;
    height: 900px;
    display: flex;
    align-items: center;
    justify-content: center;
  }
  .business-card {
    width: 900px;
    height: 560px;
    background: var(--card-bg);
    box-shadow: 0 2px 10px rgba(0,0,0,0.12);
    display: flex;
    align-items: center;
    box-sizing: border-box;
    padding: 0 70px;
  }
  .brand {
    flex: 0 0 auto;
    display: flex;
    align-items: center;
    gap: 16px;
    padding-right: 40px;
    margin-top: 110px;
  }
  .brand-mark {
    width: 32px;
    height: 32px;
    background: var(--silver-light);
    border-radius: 50%;
  }
  .brand-name {
    font-weight: 700;
    font-size: 52px;
    letter-spacing: 2px;
    color: var(--silver);
  }
  .divider {
    width: 2px;
    height: 250px;
    background: var(--rule);
    margin-top: -40px;
  }
  .contact {
    padding-left: 34px;
    margin-top: -60px;
    color: var(--silver-dark);
    font-size: 24px;
    line-height: 1.3;
  }
  .contact-name {
    font-size: 30px;
    color: var(--ink);
    text-transform: uppercase;
    letter-spacing: 0.5px;
    margin: 0 0 14px;
    font-weight: 400;
  }
  .contact-line {
    display: flex;
    align-items: center;
    gap: 12px;
    margin: 0;
  }
  .contact-line svg {
    width: 18px;
    height: 18px;
    fill: var(--ink);
  }
  .address {
    margin: 22px 0 0;
    font-style: normal;
  }
</style>
</head>
<body>
<main class="stage">
  <section class="business-card">
    <div class="brand">
      <span class="brand-mark"></span>
      <span class="brand-name">KOVALTEC</span>
    </div>
    <div class="divider"></div>
    <div class="contact">
      <h1 class="contact-name">Lena Hartwig</h1>
      <p class="contact-line">
        <svg viewBox="0 0 24 24" aria-hidden="true"><path d="M6.6 10.8a15.2 15.2 0 0 0 6.6 6.6l2.2-2.2c.3-.3.7-.4 1-.2 1.1.4 2.3.6 3.6.6.6 0 1 .4 1 1V20c0 .6-.4 1-1 1A17 17 0 0 1 3 4c0-.6.4-1 1-1h3.5c.6 0 1 .4 1 1 0 1.3.2 2.5.6 3.6.1.3 0 .7-.2 1z"/></svg>
        07163-418259-0
      </p>
      <p class="contact-line">
        <svg viewBox="0 0 24 24" aria-hidden="true"><path d="M3 5h18v14H3zm2 2v.4l7 4.6 7-4.6V7zm0 2.8V17h14V9.8l-7 4.6z"/></svg>
        lena@kovaltec-pbz.de
      </p>
      <address class="address">
        Lindkofer Str. 18<br>
        71468 Lindenbach
      </address>
    </div>
  </section>
</main>
</body>
</html>
```